Redesign of Website

We need an overhaul of our website. I've attached our current logo files. Please visit www.pelvorix.com for our current website for information about our company. We are looking for the same type of website (information-based only) so no need for any online store, payments, interactive stuff or anything like that...basically looking for a fresh new look! Also please make sure this design will be mobile-friendly. Thanks!

```html
<!DOCTYPE html>
<html lang="en">
<head>
<meta charset="utf-8">
<title>Pelvorix – Property Listings</title>
<link href="https://fonts.googleapis.com/css2?family=Montserrat:wght@400;500;600;700&family=Lato:ital,wght@0,400;0,700;1,400&display=swap" rel="stylesheet">
<style>
:root{
  --blue:#0b4a8f;
  --blue-link:#1553b8;
  --ink:#222;
  --text:#444;
  --muted:#777;
  --line:#e4e4e4;
  --panel:#f5f5f5;
  --green:#9fd09c;
  --teal:#1fa37d;
  --orange:#f39a12;
  --white:#fff;
}
*{box-sizing:border-box;margin:0;padding:0}
html,body{width:1192px;height:1200px;overflow:hidden;background:var(--white)}
body{font-family:"Lato",sans-serif;color:var(--text);position:relative}
.wrap{position:absolute;left:93px;width:1008px}

/* top bar */
.topbar{height:31px;border-bottom:1px solid var(--line);font-family:"Montserrat",sans-serif;font-size:11.5px;color:#555;position:relative}
.topbar .wrap{display:flex;align-items:center;top:0;height:31px}
.currency{display:flex;align-items:center;gap:10px}
.currency .sel{background:#f3f3f3;padding:3px 8px;color:#333}
.caret{display:inline-block;border:4px solid transparent;border-top:4px solid #333;border-bottom:0;margin-left:6px;vertical-align:middle}
.contact{display:flex;align-items:center;gap:6px;position:absolute;white-space:nowrap}
.contact svg{width:13px;height:13px;stroke:#888;fill:none;stroke-width:1.5}
.socials{position:absolute;left:826px;display:flex;gap:9px}
.socials span{width:8px;height:8px;border-radius:50%;background:#555}
.login{position:absolute;right:0;color:#666}

/* header */
.header{position:absolute;top:32px;left:0;width:1192px;height:70px}
.brand{position:absolute;left:0;top:20px;display:flex;align-items:center;gap:8px;font-family:"Montserrat",sans-serif;font-weight:700;font-size:24px;color:var(--blue)}
.brand i{width:12px;height:12px;background:var(--blue);display:block}
.nav{position:absolute;left:136px;top:27px;display:flex;gap:36px;font-family:"Montserrat",sans-serif;font-size:13.5px;color:#333;letter-spacing:.3px}
.submit{position:absolute;right:0;top:28px;font-family:"Montserrat",sans-serif;font-size:12px;font-weight:600;color:var(--blue-link);display:flex;align-items:center;gap:5px}
.submit b{width:11px;height:11px;border-radius:50%;background:var(--blue-link);color:#fff;font-size:10px;line-height:11px;text-align:center}

/* hero */
.hero{position:absolute;top:102px;left:0;width:1192px;height:532px;background:linear-gradient(90deg,#3b3b44 0%,#8f8aa0 18%,#c9c3d6 45%,#dcd7e6 60%,#b8b2c8 80%,#8c879c 100%)}
.arrow{position:absolute;top:244px;width:42px;height:42px;background:rgba(255,255,255,.55);display:flex;align-items:center;justify-content:center}
.arrow svg{width:12px;height:12px;stroke:#555;fill:none;stroke-width:1.5}
.hero-card{position:absolute;left:93px;top:227px;width:469px;height:163px;background:rgba(235,235,235,.9)}
.hero-card h1{position:absolute;left:21px;top:14px;font-family:"Montserrat",sans-serif;font-weight:700;font-size:27px;line-height:34px;color:#555}
.hero-addr{position:absolute;left:24px;top:111px;display:flex;gap:12px;font-style:italic;font-size:14px;line-height:21px;color:#333}
.hero-addr svg{width:24px;height:30px;stroke:#333;fill:none;stroke-width:1.5;margin-top:4px}
.hero-price{position:absolute;left:348px;top:326px;width:265px;height:50px;background:var(--blue);color:#fff;font-family:"Montserrat",sans-serif;font-weight:600;font-size:21px;display:flex;align-items:center;justify-content:center}

/* search */
.search{position:absolute;top:546px;left:93px;width:1008px;height:168px;background:var(--panel);border-top:6px solid var(--green)}
.field{position:absolute;top:25px;text-align:center;font-family:"Montserrat",sans-serif;font-size:11.5px;font-weight:600;color:#222}
.box{position:absolute;top:53px;height:40px;background:#fff;border:1px solid #ccc;display:flex;align-items:center;justify-content:center;font-style:italic;font-size:14px;color:#444}
.box .caret{position:absolute;right:12px}
.dash{position:absolute;left:835px;top:65px;font-size:11px;color:#999}
.mini{position:absolute;left:922px;top:22px;width:73px;height:20px;background:#fff;border:1px solid #ccc;font-size:12px;font-style:italic;display:flex;align-items:center;padding-left:4px}
.btn{position:absolute;top:116px;width:106px;height:32px;font-family:"Montserrat",sans-serif;font-size:13.5px;display:flex;align-items:center;justify-content:center;letter-spacing:.3px}
.btn.ghost{border:2px solid var(--blue);color:var(--blue);background:#fff}
.btn.solid{background:var(--blue);color:#fff}

/* sort */
.sortbar{position:absolute;top:714px;left:93px;width:1008px;height:34px;background:#eee;display:flex;align-items:center;padding-left:10px;font-size:12.5px;color:#333;gap:26px}
.sortbar .label{display:flex;gap:5px;align-items:center;margin-right:-6px}
.sortbar .on{color:var(--blue-link)}
.views{position:absolute;right:10px;display:flex;gap:12px}
.views svg{width:15px;height:13px}
.found{position:absolute;top:758px;left:93px;width:1008px;display:flex;justify-content:space-between;align-items:center}
.found h2{font-family:"Montserrat",sans-serif;font-weight:600;font-size:19px;color:#555}
.found span{font-size:13px;color:#333;margin-right:10px}

/* cards */
.cards{position:absolute;top:790px;left:93px;width:1008px;display:flex;gap:12px}
.card{width:328px;height:410px;background:var(--panel);position:relative}
.photo{height:204px;position:relative}
.tags{position:absolute;right:0;top:12px;display:flex;gap:5px}
.tag{height:22px;padding:0 9px;color:#fff;font-family:"Montserrat",sans-serif;font-weight:700;font-size:11.5px;display:flex;align-items:center}
.tag.blue{background:var(--blue)} .tag.teal{background:var(--teal)} .tag.orange{background:var(--orange)}
.star{position:absolute;left:0;top:12px;width:22px;height:22px;background:#3b8fe0;display:flex;align-items:center;justify-content:center}
.dots{position:absolute;bottom:10px;left:50%;transform:translateX(-50%);display:flex;gap:7px}
.dots i{width:6px;height:6px;border-radius:50%;background:rgba(255,255,255,.5)}
.dots i:first-child{background:#fff}
.heart{position:absolute;right:11px;bottom:11px;width:26px;height:26px;background:rgba(255,255,255,.85);display:flex;align-items:center;justify-content:center}
.heart svg{width:15px;height:14px;stroke:#444;fill:none;stroke-width:1.6}
.body{padding:11px 11px 0}
.body h3{font-family:"Montserrat",sans-serif;font-weight:700;font-size:19.5px;line-height:25px;color:var(--ink);letter-spacing:-.1px}
.addr{font-style:italic;font-size:12.5px;color:#333;margin-top:8px;display:flex;gap:4px;align-items:center;white-space:nowrap}
.addr svg{width:11px;height:12px;stroke:#555;fill:none;stroke-width:1.5}
.price{font-family:"Montserrat",sans-serif;font-weight:600;font-size:16px;color:var(--blue-link);margin-top:13px}
.specs{font-size:12.5px;color:#333;margin-top:13px;display:flex;gap:11px;white-space:nowrap}
.specs b{font-weight:700}
.foot{position:absolute;left:11px;right:11px;bottom:10px;display:flex;align-items:center;justify-content:space-between}
.ago{font-size:9.5px;color:#333;width:75px}
.compare{font-size:13px;color:#333;display:flex;gap:6px;align-items:center}
.compare svg{width:13px;height:13px;stroke:#333;fill:none;stroke-width:1.3}
.details{width:113px;height:32px;border:2px solid var(--blue);background:#fff;color:var(--blue);font-family:"Montserrat",sans-serif;font-size:13.5px;display:flex;align-items:center;justify-content:center}
</style>
</head>
<body>

<div class="topbar">
  <div class="wrap">
    <div class="currency">Currency <span class="sel">Any <span class="caret"></span></span></div>
    <div class="contact" style="left:188px">
      <svg viewBox="0 0 16 16"><path d="M4 2l2 3-1.5 1.5a8 8 0 0 0 5 5L11 10l3 2-1.5 2.5C7 14 2 9 1.5 3.5z"/></svg>555-214-7730
    </div>
    <div class="contact" style="left:320px">
      <svg viewBox="0 0 16 16"><path d="M8 15s5-5 5-9A5 5 0 0 0 3 6c0 4 5 9 5 9z"/><circle cx="8" cy="6" r="1.8"/></svg>48 Linden Ct Suite 3 , Harrow Vale, NJ 07000
    </div>
    <div class="contact" style="left:679px;font-size:12.5px;color:#444">
      <svg viewBox="0 0 16 16"><rect x="1.5" y="3.5" width="13" height="9"/><path d="M1.5 3.5l6.5 5 6.5-5"/></svg>info@pelvorix.com
    </div>
    <div class="socials"><span></span><span></span><span></span><span></span></div>
    <div class="login">Login / Register</div>
  </div>
</div>

<header class="header">
  <div class="wrap">
    <div class="brand"><i></i>Pelvorix</div>
    <nav class="nav">
      <span>HOME <span class="caret" style="margin-left:2px;border-width:3px"></span></span>
      <span>ABOUT <span class="caret" style="margin-left:2px;border-width:3px"></span></span>
      <span>CONTACTS <span class="caret" style="margin-left:2px;border-width:3px"></span></span>
      <span>SERVICES <span class="caret" style="margin-left:2px;border-width:3px"></span></span>
    </nav>
    <div class="submit">SUBMIT PROPERTY <b>+</b></div>
  </div>
</header>

<section class="hero" role="img" aria-label="Photo of a minimalist living room with white sofas, wall-mounted TV and violet ceiling lighting">
  <div class="arrow" style="left:11px"><svg viewBox="0 0 12 12"><path d="M8 1L3 6l5 5"/></svg></div>
  <div class="arrow" style="right:11px"><svg viewBox="0 0 12 12"><path d="M4 1l5 5-5 5"/></svg></div>
  <div class="hero-card">
    <h1>MINIMALIST AND BRIGHT<br>FLAT</h1>
    <div class="hero-addr">
      <svg viewBox="0 0 24 30"><path d="M12 28s10-10 10-17A10 10 0 0 0 2 11c0 7 10 17 10 17z"/><circle cx="12" cy="11" r="4"/></svg>
      <span>412-418 Ardent Ave, New<br>York, NY 10018, USA</span>
    </div>
  </div>
  <div class="hero-price">$850,000</div>
</section>

<section class="search">
  <div class="field" style="left:11px;width:314px">PROPERTY TYPE</div>
  <div class="field" style="left:346px;width:314px">OFFER TYPE</div>
  <div class="field" style="left:914px;width:0;display:flex;justify-content:center;left:842px"><span style="white-space:nowrap;position:absolute;right:-20px">PRICE</span></div>
  <div class="mini">Currency <span class="caret" style="margin-left:8px"></span></div>
  <div class="box" style="left:11px;width:314px">Property Type <span class="caret"></span></div>
  <div class="box" style="left:346px;width:314px">Offer Type <span class="caret"></span></div>
  <div class="box" style="left:681px;width:150px">From</div>
  <div class="dash">–</div>
  <div class="box" style="left:846px;width:150px">To</div>
  <div class="btn ghost" style="left:392px">CLEAR</div>
  <div class="btn solid" style="left:508px">ADVANCED</div>
</section>

<div class="sortbar">
  <span class="label">
    <svg width="12" height="12" viewBox="0 0 12 12"><path d="M3 1v10M1 9l2 2 2-2M7 2h4M7 5h3M7 8h2" stroke="#333" fill="none" stroke-width="1.2"/></svg>Sort by:
  </span>
  <span class="on">NEWEST</span><span>POPULAR</span><span>PRICE (HIGH TO LOW)</span><span>PRICE (LOW TO HIGH)</span>
  <div class="views">
    <svg viewBox="0 0 15 13"><g fill="#1553b8"><rect x="0" y="0" width="4" height="3.5"/><rect x="5.5" y="0" width="4" height="3.5"/><rect x="11" y="0" width="4" height="3.5"/><rect x="0" y="4.75" width="4" height="3.5"/><rect x="5.5" y="4.75" width="4" height="3.5"/><rect x="11" y="4.75" width="4" height="3.5"/><rect x="0" y="9.5" width="4" height="3.5"/><rect x="5.5" y="9.5" width="4" height="3.5"/><rect x="11" y="9.5" width="4" height="3.5"/></g></svg>
    <svg viewBox="0 0 15 13"><g fill="#888"><rect x="0" y="0" width="6.5" height="5.5"/><rect x="8.5" y="0" width="6.5" height="5.5"/><rect x="0" y="7.5" width="6.5" height="5.5"/><rect x="8.5" y="7.5" width="6.5" height="5.5"/></g></svg>
    <svg viewBox="0 0 15 13"><g fill="#888"><rect x="0" y="0" width="3" height="3"/><rect x="5" y="0" width="10" height="3"/><rect x="0" y="5" width="3" height="3"/><rect x="5" y="5" width="10" height="3"/><rect x="0" y="10" width="3" height="3"/><rect x="5" y="10" width="10" height="3"/></g></svg>
  </div>
</div>

<div class="found"><h2>82 FOUND</h2><span>SAVE THIS SEARCH</span></div>

<div class="cards">
  <article class="card">
    <div class="photo" role="img" aria-label="Photo of a hotel-style apartment with sofa and city view windows" style="background:linear-gradient(135deg,#5a3a2a,#b08a62 50%,#d8d2c8)">
      <div class="star"><svg width="12" height="12" viewBox="0 0 12 12"><path d="M6 .8l1.6 3.4 3.6.4-2.7 2.5.8 3.6L6 8.9 2.7 10.7l.8-3.6L.8 4.6l3.6-.4z" fill="#fff"/></svg></div>
      <div class="tags"><span class="tag teal">OPEN HOUSE</span><span class="tag blue">FOR SALE</span></div>
      <div class="dots"><i></i><i></i><i></i></div>
      <div class="heart"><svg viewBox="0 0 16 14"><path d="M8 13S1 8.5 1 4.5A3.5 3.5 0 0 1 8 3a3.5 3.5 0 0 1 7 1.5C15 8.5 8 13 8 13z"/></svg></div>
    </div>
    <div class="body">
      <h3>Modern apartment in the city center</h3>
      <div class="addr"><svg viewBox="0 0 11 12"><path d="M5.5 11s4-4 4-6.5a4 4 0 0 0-8 0C1.5 7 5.5 11 5.5 11z"/></svg>88-96 N Calder St, Chicago, IL 60607, USA</div>
      <div class="price" style="margin-top:10px;padding-left:4px">$850,000</div>
      <div class="specs" style="margin-top:16px"><span><b>Bedrooms:</b> 3</span><span><b>Bathrooms:</b> 2</span><span><b>Property size:</b> 1100 ft²</span></div>
    </div>
    <div class="foot"><span class="ago">1 year ago</span><span class="compare"><svg viewBox="0 0 13 13"><rect x="1" y="4" width="8" height="8"/><path d="M4 4V1h8v8H9"/></svg>COMPARE</span><span class="details">DETAILS ›</span></div>
  </article>

  <article class="card">
    <div class="photo" role="img" aria-label="Photo of a minimalist living room with white sofa and violet lighting" style="background:linear-gradient(135deg,#8d86a0,#d9d4e2 50%,#b7b2c2)">
      <div class="tags"><span class="tag blue">FOR SALE</span></div>
      <div class="dots"><i></i><i></i><i></i></div>
      <div class="heart"><svg viewBox="0 0 16 14"><path d="M8 13S1 8.5 1 4.5A3.5 3.5 0 0 1 8 3a3.5 3.5 0 0 1 7 1.5C15 8.5 8 13 8 13z"/></svg></div>
    </div>
    <div class="body">
      <h3>Minimalist and bright flat</h3>
      <div class="addr"><svg viewBox="0 0 11 12"><path d="M5.5 11s4-4 4-6.5a4 4 0 0 0-8 0C1.5 7 5.5 11 5.5 11z"/></svg>412-418 Ardent Ave, New York, NY 10018, USA</div>
      <div class="price">$850,000</div>
      <div class="specs"><span><b>Bedrooms:</b> 3</span><span><b>Bathrooms:</b> 2</span><span><b>Property size:</b> 1700 ft²</span></div>
    </div>
    <div class="foot"><span class="ago">1 year ago</span><span class="compare"><svg viewBox="0 0 13 13"><rect x="1" y="4" width="8" height="8"/><path d="M4 4V1h8v8H9"/></svg>COMPARE</span><span class="details">DETAILS ›</span></div>
  </article>

  <article class="card">
    <div class="photo" role="img" aria-label="Photo of a bright apartment with brown sectional sofa and striped rug" style="background:linear-gradient(135deg,#d9d7d3,#8a7766 55%,#5a4636)">
      <div class="tags"><span class="tag orange">NO FEES!</span><span class="tag blue">FOR SALE</span></div>
      <div class="dots"><i></i><i></i><i></i></div>
      <div class="heart"><svg viewBox="0 0 16 14"><path d="M8 13S1 8.5 1 4.5A3.5 3.5 0 0 1 8 3a3.5 3.5 0 0 1 7 1.5C15 8.5 8 13 8 13z"/></svg></div>
    </div>
    <div class="body">
      <h3>Bright apartment</h3>
      <div class="addr"><svg viewBox="0 0 11 12"><path d="M5.5 11s4-4 4-6.5a4 4 0 0 0-8 0C1.5 7 5.5 11 5.5 11z"/></svg>210-260 N Wrenfield Rd, Los Angeles, CA 90033, USA</div>
      <div class="price">$850,000</div>
      <div class="specs"><span><b>Bedrooms:</b> 3</span><span><b>Bathrooms:</b> 2</span><span><b>Property size:</b> 2000 ft²</span></div>
    </div>
    <div class="foot"><span class="ago">1 year ago</span><span class="compare"><svg viewBox="0 0 13 13"><rect x="1" y="4" width="8" height="8"/><path d="M4 4V1h8v8H9"/></svg>COMPARE</span><span class="details">DETAILS ›</span></div>
  </article>
</div>

</body>
</html>
```